Infographics and Newsletters for Community Advocacy and Election Campaign

**Project Overview:**
We are seeking talented designers to create a series of infographics and newsletters that will serve a dual purpose: to address community concerns, challenge corrupt leadership, and transition into a campaign for running for the elected chief position within the First Nation. The materials will be instrumental in advocating for change, raising awareness about critical issues, and laying the foundation for a successful election campaign.
**Project Goals:**
1. **Advocate** for addressing community concerns and challenging corrupt leadership.
2. **Educate** community members about the need for change and transparency in leadership.
3. **Prepare** campaign materials for running for the elected chief position.
**Target Audience:**
- Registered members of the First Nation
- Elected council members
**Key Messages to Convey:**
1. Addressing specific community concerns and issues.
2. Challenging corrupt leadership and advocating for transparency.
3. Outlining a vision for positive change and effective leadership.
4. Transitioning the materials into a campaign for the elected chief position.
**Design Requirements:**
1. **Infographics:**
- Visual representation of community concerns, corrupt leadership challenges, and proposed solutions.
- Engaging visuals and clear messaging to resonate with the audience.
- Incorporate the community’s branding elements and color scheme.
- **Design Elements:**
- White background with colorful leaves (yellow, red, blue, green, lavender) that are partially eaten by caterpillars.
- Caterpillars labeled with names like "Corruption" to symbolize the issues being addressed.
- A tree with a path leading towards "Unity" to symbolize the vision for positive change.
2. **Newsletters:**
- Detailed information on community concerns, proposed solutions, and campaign messages.
- Sections for updates on advocacy efforts and campaign progress.
- Space for community feedback and engagement.
- **Design Elements:**
- Use the same color scheme (yellow, red, blue, green, lavender, black, and white).
- Incorporate the tree and path towards "Unity" as a recurring theme.
**Language Requirement:**
- Designs and content to be created in both English and Quebec French.
**Preferred Color Scheme and Branding:**
- Yellow, red, blue, green, lavender, black, and white.
- Reflect the Seloru Kwemotan Nation’s identity and values.
- Incorporate the community’s logo and branding elements.
**Deliverables:**
1. Two infographics in high-resolution format (PDF and PNG) in both English and Quebec French.
2. Two newsletter templates in editable format (Word or InDesign) in both English and Quebec French.
3. All design files and assets used in the creation of the infographics and newsletters.
**Additional Information:**
- The materials will be used to advocate for change, challenge corrupt leadership, and transition into a campaign for the elected chief position.
- Designers with experience in community advocacy and election campaign materials are preferred.

```html
<!DOCTYPE html>
<html lang="en">
<head>
<meta charset="utf-8">
<title>Community Concerns – Path to Unity</title>
<link href="https://fonts.googleapis.com/css2?family=Anton&family=Poppins:wght@300;600&display=swap" rel="stylesheet">
<style>
  :root{
    --paper:#fcfbfa;
    --ink:#2b2b2b;
    --body:#4a4a4a;
    --green:#16a047;
    --red:#c8161d;
    --yellow:#eab814;
    --blue:#1878c2;
    --lavender:#9a5cf0;
    --violet:#4d5cff;
    --dots:#333;
  }
  *{box-sizing:border-box;margin:0;padding:0}
  html,body{width:1200px;height:732px;overflow:hidden;background:var(--paper)}
  body{font-family:"Poppins",sans-serif;color:var(--ink)}
  .infographic{position:relative;width:1200px;height:732px;background:var(--paper);overflow:hidden}
  .path-line{position:absolute;inset:0;width:1200px;height:732px}
  .concern{position:absolute;z-index:3}
  .concern h2{font-weight:600;font-size:25px;line-height:1.1;letter-spacing:-.2px;color:var(--ink)}
  .concern p{font-weight:300;font-size:17px;line-height:22px;color:var(--body);margin-top:6px;width:200px}
  .icon{position:absolute;fill:none;stroke-width:2.4;stroke-linecap:round;stroke-linejoin:round}
  .leaf{position:absolute;border-radius:50% 8% 50% 8%}
  .leaf--green{left:72px;top:384px;width:160px;height:186px;background:radial-gradient(circle at 55% 40%,#9fd66a 0 22%,var(--green) 50%,#0f7a35)}
  .leaf--red{left:308px;top:136px;width:138px;height:180px;background:radial-gradient(circle at 50% 30%,#9fd66a 0 22%,var(--red) 50%,#9c0f14)}
  .leaf--yellow{left:426px;top:366px;width:150px;height:170px;background:radial-gradient(circle at 50% 30%,#9fd66a 0 22%,var(--yellow) 50%,#c99a0c)}
  .leaf--blue{left:624px;top:541px;width:152px;height:140px;background:radial-gradient(circle at 55% 35%,#9fd66a 0 22%,var(--blue) 50%,#0f5c99)}
  .unity-tree{position:absolute;left:752px;top:55px;width:432px;height:463px;border-radius:40% 40% 10% 10%;
    background:linear-gradient(90deg,#3f8fe0 0%,#5ec248 35%,#f3a11c 65%,#e0417a 100%);opacity:.85}
  .unity-word{position:absolute;left:803px;top:64px;z-index:2;
    font-family:"Anton",sans-serif;font-size:245px;line-height:1;letter-spacing:2px;
    background:linear-gradient(90deg,var(--violet),var(--lavender));
    -webkit-background-clip:text;background-clip:text;color:transparent;
    -webkit-text-stroke:2px #fff;
    transform:scaleX(.67);transform-origin:left top;white-space:nowrap}
  .nation-name{position:absolute;left:1030px;top:600px;width:150px;display:flex;flex-direction:column;align-items:center;gap:8px}
  .nation-name .mark{width:44px;height:44px;border-radius:50%;background:#1f3e73}
  .nation-name span{font-weight:600;font-size:14px;line-height:1.2;text-align:center;color:#1f3e73;text-transform:uppercase}
</style>
</head>
<body>
<main class="infographic">

  <svg class="path-line" viewBox="115 120 2235 1257" preserveAspectRatio="none" aria-hidden="true">
    <g fill="none" stroke="var(--dots)" stroke-width="2" stroke-dasharray="1 6" stroke-linecap="round">
      <path d="M555 885 C620 840 640 760 632 640 C625 560 640 500 690 488" vector-effect="non-scaling-stroke"/>
      <path d="M980 630 C1050 700 1120 770 1200 778 C1270 780 1280 680 1220 655 C1150 630 1080 690 1075 780" vector-effect="non-scaling-stroke"/>
      <path d="M1110 1040 C1150 1110 1220 1160 1290 1165" vector-effect="non-scaling-stroke"/>
      <path d="M1540 1100 C1620 1040 1640 940 1625 860 C1605 780 1585 740 1590 700" vector-effect="non-scaling-stroke"/>
    </g>
  </svg>

  <div class="leaf leaf--green" role="img" aria-label="Illustration of a caterpillar eating a green leaf"></div>
  <div class="leaf leaf--red" role="img" aria-label="Illustration of a caterpillar eating a red leaf"></div>
  <div class="leaf leaf--yellow" role="img" aria-label="Illustration of a caterpillar eating a yellow leaf"></div>
  <div class="leaf leaf--blue" role="img" aria-label="Illustration of a caterpillar eating a blue leaf"></div>

  <div class="unity-tree" role="img" aria-label="Rainbow-leaved tree on a coloured base"></div>
  <div class="unity-word">UNITY</div>

  <svg class="icon" style="left:176px;top:206px" width="68" height="72" viewBox="0 0 68 72" stroke="var(--green)" aria-hidden="true">
    <circle cx="30" cy="38" r="27"/>
    <line x1="11" y1="19" x2="49" y2="57"/>
    <rect x="18" y="30" width="22" height="14"/>
    <path d="M42 20 h20 v24 h-14 l-4 -6 h-6"/>
  </svg>
  <section class="concern" style="left:34px;top:264px">
    <h2>Corruption</h2>
    <p>Lorem ipsum dolor sit amet, consectetur adipiscing elit, sed do</p>
  </section>

  <svg class="icon" style="left:588px;top:44px" width="70" height="72" viewBox="0 0 70 72" stroke="var(--red)" aria-hidden="true">
    <line x1="4" y1="14" x2="66" y2="14"/>
    <path d="M28 6 h12 v12 h-12z"/>
    <path d="M30 18 v52 h10 v-52"/>
    <line x1="10" y1="14" x2="10" y2="28"/><path d="M2 40 a8 8 0 0 0 16 0z"/><line x1="10" y1="28" x2="2" y2="40"/><line x1="10" y1="28" x2="18" y2="40"/>
    <line x1="58" y1="30" x2="58" y2="44"/><path d="M50 56 a8 8 0 0 0 16 0z"/><line x1="58" y1="44" x2="50" y2="56"/><line x1="58" y1="44" x2="66" y2="56"/>
  </svg>
  <section class="concern" style="left:463px;top:95px">
    <h2>Unjustice</h2>
    <p>Lorem ipsum dolor sit amet, consectetur adipiscing elit, sed do</p>
  </section>

  <svg class="icon" style="left:235px;top:579px" width="60" height="62" viewBox="0 0 60 62" stroke="var(--yellow)" aria-hidden="true">
    <rect x="2" y="12" width="46" height="34" rx="2"/>
    <path d="M16 12 v-8 h18 v8"/>
    <line x1="2" y1="26" x2="48" y2="26"/>
    <circle cx="44" cy="46" r="13" fill="var(--paper)"/>
    <line x1="36" y1="54" x2="52" y2="38"/>
  </svg>
  <section class="concern" style="left:306px;top:556px">
    <h2>Unemployment</h2>
    <p>Lorem ipsum dolor sit amet, consectetur adipiscing elit, sed do</p>
  </section>

  <svg class="icon" style="left:890px;top:544px" width="58" height="64" viewBox="0 0 58 64" stroke="var(--blue)" aria-hidden="true">
    <path d="M18 6 h22 v18 l-4 10 h-14 l-4 -10z"/>
    <line x1="24" y1="6" x2="24" y2="16"/><line x1="30" y1="6" x2="30" y2="16"/><line x1="36" y1="6" x2="36" y2="16"/>
    <rect x="4" y="44" width="20" height="10" rx="5"/>
    <rect x="34" y="44" width="20" height="10" rx="5"/>
    <line x1="24" y1="49" x2="34" y2="49"/>
  </svg>
  <section class="concern" style="left:792px;top:587px">
    <h2>Racism</h2>
    <p>Lorem ipsum dolor sit amet, consectetur adipiscing elit, sed do</p>
  </section>

  <div class="nation-name">
    <div class="mark"></div>
    <span>Seloru Kwemotan Nation</span>
  </div>

</main>
</body>
</html>
```